Newly established winery needs label for its bottles

The Corvel-Tamarin Winery, is a small family owned winery that has been producing wine for little over 3 years. We are now ready to officially start commercializing our products. To do so we are looking for a label for our wine bottles. We are looking for a creative design that will differentiate our bottles from the more conventional labels. We are looking for one label design with 3 color schemes so that we can have a standard look and feel for all three of our wines, while having some differentiation between them with the different color schemes. In summary we are looking for a label that will standout by its uniqueness, simplicity and its modern touch. The label should also reflect the historical significance of the name of the winery. The attached documents offers more detail about the winery, what we are looking for, as well as some technical specification for the label. This label project is also related to a logo project see brief: http://www.pitchvault.ca/project-progress.aspx?briefId=462193). The logo project is now complete and the winning design source files were added to the documents in this brief. Also, details around the information that will need to appear on the label was added to the document list.
Updates
This label project will be on hold temporarily while the logo project is in progress. If you are interested in participating in the logo project, please follow this link: http://www.pitchvault.ca/project-progress.aspx?briefId=462193 Added Wednesday, December 17, 2014
Reason: Deadline extended to give sufficent time for submission and modification to the designs provided.

```html
<!DOCTYPE html>
<html lang="fr">
<head>
<meta charset="utf-8">
<title>Corvel-Tamarin Winery – Label System</title>
<link rel="stylesheet" href="https://fonts.googleapis.com/css2?family=Arvo:wght@400;700&family=Source+Sans+3:wght@400;600;700&display=swap">
<style>
  :root {
    --blanc: #9cac6e;
    --rose: #d19292;
    --rouge: #b0493a;
    --ink-grey: #6b6c6e;
    --paper: #ffffff;
    --label-text: #ffffff;
    --tote-canvas: #f2eee4;
    --tote-print: #4e4e4e;
    --tote-ink: #ebe5d5;
    --slab: "Arvo", Georgia, serif;
    --sans: "Source Sans 3", Arial, sans-serif;
  }
  * { box-sizing: border-box; margin: 0; padding: 0; }
  html, body { width: 1200px; height: 828px; overflow: hidden; background: var(--paper); }
  .sheet { position: relative; width: 1200px; height: 828px; font-family: var(--sans); }

  .section-title {
    position: absolute; left: 74px; font: 700 10px var(--sans); color: #222;
  }
  .section-title.front { top: 14px; }
  .section-title.back { top: 434px; left: 78px; }

  /* Front labels */
  .front-label {
    position: absolute; top: 41px; width: 216px; height: 275px;
    color: var(--label-text); overflow: hidden;
  }
  .front-label.blanc { left: 73px; background: var(--blanc); }
  .front-label.rose { left: 353px; background: var(--rose); }
  .front-label.rouge { left: 615px; background: var(--rouge); }

  .front-label .house {
    position: absolute; top: 5px; width: 100%; text-align: center;
    font: 700 11px var(--slab); letter-spacing: 2px;
  }
  .front-label .estate-name {
    position: absolute; top: 30px; left: 8px;
    font: 700 44px/1 var(--slab); letter-spacing: -1px;
  }
  .front-label .estate-name span { display: block; }
  .front-label .estate-name span + span { margin-left: 4px; margin-top: 6px; }
  .front-label .winery {
    position: absolute; top: 166px; left: 46px;
    font: 700 11px var(--slab); letter-spacing: 2px;
  }
  .front-label .scene {
    position: absolute; left: 0; right: 0; bottom: 0; height: 108px;
    background: linear-gradient(to bottom, rgba(255,255,255,0) 0%, rgba(255,255,255,0.22) 70%, rgba(255,255,255,0.55) 100%);
  }
  .front-label .volume {
    position: absolute; top: 228px; right: 12px; text-align: right;
    font: 700 7px/1.5 var(--sans);
  }
  .front-label .volume small { display: block; font-size: 5px; font-weight: 400; }

  .variety {
    position: absolute; top: 330px; width: 216px; text-align: center;
  }
  .variety.blanc { left: 73px; color: var(--blanc); }
  .variety.rose { left: 353px; color: var(--rose); }
  .variety.rouge { left: 615px; color: var(--rouge); }
  .variety .fr { font: 700 21px/1 var(--slab); letter-spacing: 1px; }
  .variety .en { font: 700 14px/1 var(--slab); letter-spacing: 1.5px; color: var(--ink-grey); margin-top: 1px; }
  .variety .origin {
    margin-top: 12px; font: 600 7.5px var(--sans);
    display: flex; justify-content: center; align-items: center; gap: 6px;
  }
  .variety.rouge .origin { justify-content: flex-start; padding-left: 0; }
  .origin .mark { width: 7px; height: 7px; background: currentColor; }

  /* Back labels */
  .back-label {
    position: absolute; width: 205px; color: var(--label-text);
    padding: 0 10px;
  }
  .back-label.blanc { left: 76px; top: 458px; height: 355px; background: var(--blanc); }
  .back-label.rose { left: 350px; top: 455px; height: 355px; background: var(--rose); }
  .back-label.rouge { left: 616px; top: 455px; height: 355px; background: var(--rouge); }

  .back-label .flock {
    position: absolute; top: 10px; left: 10px; right: 10px; height: 70px;
    background: linear-gradient(to right, rgba(255,255,255,0.15), rgba(255,255,255,0.4));
  }
  .back-label .copy {
    position: absolute; left: 10px; right: 8px;
    font: 600 8.6px/1.3 var(--sans);
  }
  .back-label .copy.fr { top: 90px; }
  .back-label .copy.en { top: 180px; }
  .back-label .copy p + p { margin-top: 14px; }
  .back-label .signature {
    position: absolute; top: 282px; width: 100%; left: 0; text-align: center;
    font: 700 13px var(--sans); letter-spacing: 0.3px;
  }
  .back-label .address {
    position: absolute; top: 306px; width: 100%; left: 0; text-align: center;
    font: 700 9px/1.3 var(--sans);
  }

  /* Tote print */
  .tote-print {
    position: absolute; left: 950px; top: 458px; width: 152px; height: 102px;
    background: var(--tote-canvas); padding: 6px;
  }
  .tote-print .panel {
    position: relative; width: 100%; height: 100%; background: var(--tote-print); color: var(--tote-ink);
  }
  .tote-print .estate-name {
    position: absolute; top: 5px; left: 8px; font: 700 17px/1 var(--slab);
  }
  .tote-print .estate-name span { display: block; }
  .tote-print .estate-name span + span { margin-top: 2px; }
  .tote-print .scene {
    position: absolute; right: 8px; top: 24px; width: 40px; height: 36px;
    background: linear-gradient(to bottom, rgba(235,229,213,0.1), rgba(235,229,213,0.45));
  }
  .tote-print .house {
    position: absolute; top: 66px; width: 100%; text-align: center;
    font: 700 11px var(--slab); letter-spacing: 1.5px;
  }
  .tote-print .origin {
    position: absolute; top: 80px; width: 100%;
    display: flex; justify-content: center; align-items: center; gap: 4px;
    font: 600 4.5px var(--sans);
  }
  .tote-print .origin .mark { width: 4px; height: 4px; background: currentColor; }
</style>
</head>
<body>
<main class="sheet">

  <h2 class="section-title front">Front Design 7.5"x4.5"</h2>

  <section class="front-label blanc">
    <div class="house">VIGNOBLE</div>
    <div class="estate-name"><span>Corvel</span><span>Tamarin</span></div>
    <div class="winery">WINERY</div>
    <div class="scene" role="img" aria-label="White silhouette of a windmill, barn, bird and grass"></div>
    <div class="volume">740ml<small>11.8% alc./Vol.</small></div>
  </section>
  <section class="front-label rose">
    <div class="house">VIGNOBLE</div>
    <div class="estate-name"><span>Corvel</span><span>Tamarin</span></div>
    <div class="winery">WINERY</div>
    <div class="scene" role="img" aria-label="White silhouette of a windmill, barn, bird and grass"></div>
    <div class="volume">740ml<small>11.8% alc./Vol.</small></div>
  </section>
  <section class="front-label rouge">
    <div class="house">VIGNOBLE</div>
    <div class="estate-name"><span>Corvel</span><span>Tamarin</span></div>
    <div class="winery">WINERY</div>
    <div class="scene" role="img" aria-label="White silhouette of a windmill, barn, bird and grass"></div>
    <div class="volume">740ml<small>11.4% alc./Vol.</small></div>
  </section>

  <div class="variety blanc">
    <div class="fr">VIN BLANC</div>
    <div class="en">WHITE WINE</div>
    <div class="origin"><span>Produit du Québec</span><span class="mark"></span><span>Product of Québec</span></div>
  </div>
  <div class="variety rose">
    <div class="fr">VIN ROSÉ</div>
    <div class="en">BLUSH WINE</div>
    <div class="origin"><span>Produit du Québec</span><span class="mark"></span><span>Product of Québec</span></div>
  </div>
  <div class="variety rouge">
    <div class="fr">VIN ROUGE</div>
    <div class="en" style="color:var(--rouge)">RED WINE</div>
    <div class="origin"><span>Produit du Québec</span><span class="mark"></span><span>Product of Québec</span></div>
  </div>

  <h2 class="section-title back">Back Design 7.5"x4.5"</h2>

  <section class="back-label blanc">
    <div class="flock" role="img" aria-label="White silhouettes of birds in flight"></div>
    <div class="copy fr">
      <p>Cultivé et mis en Vignoble Corvel-Tamarin. Ce vin blanc est d'intensité moyenne et légèrement soutenu. Il accompagne très bien les fruits de mer, le poisson et les différents desserts.</p>
      <p>Contient des sulfites</p>
    </div>
    <div class="copy en">
      <p>Grown &amp; bottled at the Corvel-Tamarin Vineyard. This white wine has a medium intensity &amp; is slightly supported. It accompanies well seafood, fish, sushi, as well as dessert.</p>
      <p>Contains sulphates</p>
    </div>
    <div class="signature">Vignoble Corvel-Tamarin senc.</div>
    <div class="address">48 Chemin Brisebois<br>St-Aurèle-des-Champs Qc<br>J0J 2K4</div>
  </section>
  <section class="back-label rose">
    <div class="flock" role="img" aria-label="White silhouettes of birds in flight"></div>
    <div class="copy fr">
      <p>Cultivé et mis en Vignoble Corvel-Tamarin. Ce vin blanc est d'intensité moyenne et légèrement soutenu. Il accompagne très bien les fruits de mer, le poisson et les différents desserts.</p>
      <p>Contient des sulfites</p>
    </div>
    <div class="copy en">
      <p>Grown &amp; bottled at the Corvel-Tamarin Vineyard. This white wine has a medium intensity &amp; is slightly supported. It accompanies well seafood, fish, sushi, as well as dessert.</p>
      <p>Contains sulphates</p>
    </div>
    <div class="signature">Vignoble Corvel-Tamarin senc.</div>
    <div class="address">48 Chemin Brisebois<br>St-Aurèle-des-Champs Qc<br>J0J 2K4</div>
  </section>
  <section class="back-label rouge">
    <div class="flock" role="img" aria-label="White silhouettes of birds in flight"></div>
    <div class="copy fr">
      <p>Cultivé et mis en Vignoble Corvel-Tamarin. Ce vin blanc est d'intensité moyenne et légèrement soutenu. Il accompagne très bien les fruits de mer, le poisson et les différents desserts.</p>
      <p>Contient des sulfites</p>
    </div>
    <div class="copy en">
      <p>Grown &amp; bottled at the Corvel-Tamarin Vineyard. This white wine has a medium intensity &amp; is slightly supported. It accompanies well seafood, fish, sushi, as well as dessert.</p>
      <p>Contains sulphates</p>
    </div>
    <div class="signature">Vignoble Corvel-Tamarin senc.</div>
    <div class="address">48 Chemin Brisebois<br>St-Aurèle-des-Champs Qc<br>J0J 2K4</div>
  </section>

  <section class="tote-print">
    <div class="panel">
      <div class="estate-name"><span>Corvel</span><span>Tamarin</span></div>
      <div class="scene" role="img" aria-label="Windmill and grass silhouette"></div>
      <div class="house">VIGNOBLE</div>
      <div class="origin"><span>Produit du Québec</span><span class="mark"></span><span>Product of Québec</span></div>
    </div>
  </section>

</main>
</body>
</html>
```